Webdesign/Scribble/Layout eines mehrstufigen Formulars
Zielgruppe
Wir sind ein Startup, das über die Seite Planovia.de zukünftig folgenden Service anbietet: Unternehmer können sehr flexibel (selbst) gestaltete Terminformulare erstellen und auf Ihrer Website einbinden. Kunden können dann diese Termine buchen und bekommen dann Erinnerungs-Mails und SMS.
Zielgruppe: Dienstleister wie Fotografen, Friseure, Versicherungsvertreter, Masseure, Restaurants, Arztpraxen. Also alle, die darauf angewiesen sind, dass vereinbarte Termine eingehalten werden und die die Terminvereinbarung vereinfachen wollen. Also weniger per Telefon, mehr über die eigene Website.
Siehe auch: https://www.clipwelt.de/watch?v=Qm7TzRk2pLx
Siehe auch: https://www.clipwelt.de/watch?v=Wn4HsVd8oYe
Aufgabenstellung
Wir benötigen KEIN komplettes Webdesign!!!
Es geht lediglich um ein Scribble/Design bezüglich unseres Termin-Assistenten auf https://dev.planovia.de/de/schnellstart.html (oder siehe jpg auf https://ablage.wolkenfach.de/ordner/8Xr2Kp0Lq5Tz9Vb3Nw6Hs1Jd4Fm7Yc?freigabe=ja )
Dieses Scribble/Design soll dann unser Programmierer umsetzen können auf https://dev.planovia.de/de/schnellstart.html
-- Was ist der Termin-Assistent? --
Der Termin-Assistent führt den User durch den Terminformular-Prozess (siehe unten). Mit seiner Hilfe erhält der User am Ende ein funktionierendes Terminformular. Das aktuelle Design des Termin-Assistenten hat der Programmierer erstellt. Jetzt möchten wir es durch ein ansprechendes Design ersetzen. UX und Usability sind hierbei sehr wichtig. Der VIA (Comic-Figur auf der rechten Seite) wird später durch ein Erklärvideo/Screencast ersetzt. In diesem führt der Comic-VIA durch den Termin-Assistenten und erklärt die einzelnen Schritte bis zum gewünschten Terminformular. Eine ansprechende Verknüpfung/Einbindung von Termin-Assistent und Erklärvideo (rechts daneben, an der Stelle, wo der Comic-VIA aktuell steht), wird also bitte benötigt.
Testen können Sie den Termin-Assistenten auf https://dev.planovia.de/de/schnellstart.html
Wir benötigen also eine kreative Idee /Design/Scribble bzgl. https://ablage.wolkenfach.de/ordner/8Xr2Kp0Lq5Tz9Vb3Nw6Hs1Jd4Fm7Yc?freigabe=ja bzw. siehe bitte Terminformular-Assistent auf https://dev.planovia.de/de/schnellstart.html
Der Prozess/Ablauf des Terminformular-Assistenten kann, wenn es der Usability zugute kommt, geändert werden (ggf. ist vorab eine Rücksprache mit dem Programmierer sinnvoll. E-Mail siehe unten. Es geht um eine grafische Aufwertung und bessere Übersichtlichkeit/Bedienbarkeit (Buttons, Aufbau, Design-Elemente) sowie ein stimmige Verbindung von Termin-Assistent und Erklärvideo (rechts daneben, a..

```html
<!DOCTYPE html>
<html lang="de">
<head>
<meta charset="utf-8">
<title>Planovia – Bewerber &amp; Termine</title>
<link rel="stylesheet" href="https://fonts.googleapis.com/css2?family=Roboto:ital,wght@0,400;0,500;0,700;1,400&family=Roboto+Condensed:wght@400&display=swap">
<style>
:root{
  --canvas:#dcdcdc;
  --white:#ffffff;
  --green:#7fbc17;
  --green-dark:#6da712;
  --slate:#7c868c;
  --orange:#f39200;
  --ink:#333333;
  --ink-soft:#555555;
  --line:#b9b9b9;
  --muted-row:#7a7a7a;
  --light-band:#f6f6f6;
  --help:#d8d8d8;
  --blue:#1db1ec;
}
*{box-sizing:border-box;margin:0;padding:0}
html,body{width:1200px;height:3972px;overflow:hidden;background:var(--canvas)}
body{font-family:"Roboto",Arial,sans-serif;color:var(--ink)}
.page{position:absolute;left:205px;top:14px;width:789px;height:3945px;background:var(--white)}
.abs{position:absolute}
.site-header{left:0;top:0;width:789px;height:210px;background:var(--white)}
.brand{left:36px;top:60px;display:flex;align-items:center;gap:18px}
.brand-mark{width:54px;height:54px;background:var(--slate);border-radius:6px}
.brand-name{font-size:64px;font-weight:500;color:var(--slate);line-height:1}
.menu-button{left:624px;top:51px;width:138px;height:114px;background:var(--green)}
.menu-button span{position:absolute;left:33px;width:72px;height:5px;background:var(--white);border-radius:2px}
.hero{left:0;top:210px;width:789px;height:240px;background:var(--slate);color:var(--white);
  font-family:"Roboto Condensed",Arial,sans-serif;font-size:63px;line-height:88px;padding:36px 0 0 27px;letter-spacing:-0.5px}
.steps{left:0;top:450px;width:789px;height:408px;background:var(--green);color:var(--white)}
.steps-intro{left:27px;top:38px;font-size:46px;line-height:57px}
.step-select{left:21px;top:195px;width:744px;height:150px;background:var(--white);display:flex;align-items:center;padding-left:30px;color:var(--orange)}
.step-num{width:108px;height:108px;border:4px solid var(--orange);border-radius:50%;display:flex;align-items:center;justify-content:center;font-size:54px;font-weight:500}
.step-label{margin-left:30px;font-size:48px;font-weight:500;letter-spacing:0.5px}
.step-caret{position:absolute;right:33px;top:58px}
.heading{left:27px;top:906px;font-size:63px;font-weight:400;color:var(--ink)}
.band{left:0;width:789px}
.band.light{background:var(--light-band)}
.field-label{left:27px;font-size:48px;color:var(--ink)}
.select{left:24px;width:630px;height:105px;border:3px solid var(--line);background:var(--white);display:flex;align-items:center;padding-left:24px;font-size:44px;color:var(--ink-soft)}
.select svg.icon{margin-right:24px;flex:none}
.select .caret{position:absolute;right:30px;top:42px}
.help{left:693px;width:54px;height:54px;border-radius:50%;background:var(--help);color:#8a8a8a;font-size:36px;font-weight:500;display:flex;align-items:center;justify-content:center}
.day-panel{left:0;top:1749px;width:789px;height:1935px;background:var(--green);color:var(--white)}
.day-title{left:27px;top:56px;font-size:51px;font-weight:500}
.day-panel .select{top:132px;height:105px}
.day-panel .help{top:158px;background:#e6e6e6}
.day-note{left:27px;top:261px;font-size:46px;font-style:italic;line-height:59px;width:640px}
.slot{left:24px;width:729px;height:114px;display:flex;align-items:center;padding-left:21px;font-size:54px}
.slot.off{background:var(--muted-row)}
.box{width:69px;height:69px;background:var(--white);border-radius:4px;margin-right:39px;display:flex;align-items:center;justify-content:center;flex:none}
.footer-area{left:0;top:3684px;width:789px;height:261px;background:var(--white)}
.next-button{left:42px;top:60px;width:705px;height:132px;background:var(--blue);color:var(--white);font-size:42px;font-weight:700;letter-spacing:2px;display:flex;align-items:center;justify-content:center}
</style>
</head>
<body>
<main class="page">
  <header class="abs site-header">
    <div class="abs brand"><span class="brand-mark"></span><span class="brand-name">Planovia</span></div>
    <div class="abs menu-button" aria-label="Menü">
      <span style="top:37px"></span><span style="top:55px"></span><span style="top:73px"></span>
    </div>
  </header>

  <section class="abs hero">Das Termin-Tool für die<br>Online-Terminvereinbarung</section>

  <section class="abs steps">
    <p class="abs steps-intro">Bitte füllen Sie der Reihe nach die<br>einzelnen Formularmasken aus:</p>
    <div class="abs step-select">
      <span class="step-num">3</span>
      <span class="step-label">Bewerber &amp; Termine</span>
      <svg class="step-caret" width="30" height="30" viewBox="0 0 30 30"><path d="M2 4h26L15 28z" fill="var(--orange)"/></svg>
    </div>
  </section>

  <h2 class="abs heading">Bewerber und Termine</h2>

  <div class="abs field-label" style="top:1030px">Anzahl der Bewerber</div>
  <div class="abs select" style="top:1095px">
    <svg class="icon" width="66" height="42" viewBox="0 0 66 42"><circle cx="33" cy="11" r="9" fill="#444"/><path d="M17 40c0-11 7-17 16-17s16 6 16 17z" fill="#444"/><circle cx="14" cy="14" r="7" fill="#444"/><path d="M1 38c0-9 5-13 13-13 3 0 5 1 6 2-3 3-4 7-4 11z" fill="#444"/><circle cx="52" cy="14" r="7" fill="#444"/><path d="M65 38c0-9-5-13-13-13-3 0-5 1-6 2 3 3 4 7 4 11z" fill="#444"/></svg>
    Unbegrenzt
    <svg class="caret" width="20" height="16" viewBox="0 0 20 16"><path d="M0 0h20L10 16z" fill="#333"/></svg>
  </div>
  <div class="abs help" style="top:1121px">?</div>

  <div class="abs band light" style="top:1245px;height:231px"></div>
  <div class="abs field-label" style="top:1286px">Bewerberbungszeitraum</div>
  <div class="abs select" style="top:1338px">
    <svg class="icon" width="48" height="48" viewBox="0 0 48 48"><circle cx="24" cy="24" r="20" fill="none" stroke="#444" stroke-width="4"/><path d="M24 12v13l9 6" fill="none" stroke="#444" stroke-width="4" stroke-linecap="round"/></svg>
    Pro Stunde
    <svg class="caret" width="20" height="16" viewBox="0 0 20 16"><path d="M0 0h20L10 16z" fill="#333"/></svg>
  </div>
  <div class="abs help" style="top:1364px">?</div>

  <div class="abs field-label" style="top:1526px">Warteliste</div>
  <div class="abs select" style="top:1581px">
    <svg class="icon" width="42" height="50" viewBox="0 0 42 50"><rect x="3" y="3" width="36" height="44" rx="3" fill="none" stroke="#444" stroke-width="4"/><path d="M11 15h20M11 25h20M11 35h20" stroke="#444" stroke-width="4"/></svg>
    Nein
    <svg class="caret" width="20" height="16" viewBox="0 0 20 16"><path d="M0 0h20L10 16z" fill="#333"/></svg>
  </div>
  <div class="abs help" style="top:1607px">?</div>

  <section class="abs day-panel">
    <h3 class="abs day-title">Wählen Sie den Tag aus:</h3>
    <div class="abs select">
      <svg class="icon" width="50" height="48" viewBox="0 0 50 48"><rect x="3" y="7" width="44" height="38" rx="3" fill="none" stroke="#444" stroke-width="4"/><path d="M3 17h44M14 2v10M36 2v10M11 25h6M22 25h6M33 25h6M11 34h6M22 34h6M33 34h6" stroke="#444" stroke-width="4"/></svg>
      Mo, 07.10.2018
      <svg class="caret" width="20" height="16" viewBox="0 0 20 16"><path d="M0 0h20L10 16z" fill="#333"/></svg>
    </div>
    <div class="abs help">?</div>
    <p class="abs day-note">Sie können jeden Termin am gewählten Tag&nbsp; ein- bzw. ausschließen:</p>

    <div class="abs slot" style="top:470px"><span class="box"><svg width="50" height="40" viewBox="0 0 50 40"><path d="M4 21l14 14L46 5" fill="none" stroke="var(--green)" stroke-width="8"/></svg></span>08:00 - 09:00</div>
    <div class="abs slot off" style="top:614px"><span class="box"></span>09:00 - 10:00</div>
    <div class="abs slot" style="top:758px"><span class="box"><svg width="50" height="40" viewBox="0 0 50 40"><path d="M4 21l14 14L46 5" fill="none" stroke="var(--green)" stroke-width="8"/></svg></span>10:00 - 11:00</div>
    <div class="abs slot off" style="top:902px"><span class="box"></span>11:00 - 12:00</div>
    <div class="abs slot" style="top:1046px"><span class="box"><svg width="50" height="40" viewBox="0 0 50 40"><path d="M4 21l14 14L46 5" fill="none" stroke="var(--green)" stroke-width="8"/></svg></span>12:00 - 13:00</div>
    <div class="abs slot" style="top:1190px"><span class="box"><svg width="50" height="40" viewBox="0 0 50 40"><path d="M4 21l14 14L46 5" fill="none" stroke="var(--green)" stroke-width="8"/></svg></span>13:00 - 14:00</div>
    <div class="abs slot" style="top:1334px"><span class="box"><svg width="50" height="40" viewBox="0 0 50 40"><path d="M4 21l14 14L46 5" fill="none" stroke="var(--green)" stroke-width="8"/></svg></span>14:00 - 15:00</div>
    <div class="abs slot" style="top:1478px"><span class="box"><svg width="50" height="40" viewBox="0 0 50 40"><path d="M4 21l14 14L46 5" fill="none" stroke="var(--green)" stroke-width="8"/></svg></span>15:00 - 16:00</div>
    <div class="abs slot" style="top:1622px"><span class="box"><svg width="50" height="40" viewBox="0 0 50 40"><path d="M4 21l14 14L46 5" fill="none" stroke="var(--green)" stroke-width="8"/></svg></span>16:00 - 17:00</div>
    <div class="abs slot" style="top:1766px"><span class="box"><svg width="50" height="40" viewBox="0 0 50 40"><path d="M4 21l14 14L46 5" fill="none" stroke="var(--green)" stroke-width="8"/></svg></span>17:00 - 18:00</div>
  </section>

  <footer class="abs footer-area">
    <div class="abs next-button">» WEITER</div>
  </footer>
</main>
</body>
</html>
```